Long Established Local Fencing (not swords) Business needs fresh Business Cards

We need fresh double sided business cards for our Fencing Construction business, we are looking for something with our new logo design added, and maybe a photo background ?
We recently had cards made from Cardlyne and we were horrified with what we got back, the quality was terrible, so am looking for high quality format for good printing company to make.
We install Steelmora, Timber paling, Aluminium Slat Screening, Picket (timber and aluminium) and most other fencing installations.
Our website is brankelrails.com.au should you like to learn a bit more.
We do have logo in other formats if required.
We have been in business for over 35 years and we have used this as a "motto" it is on our signage

Industry/Entity Type

Construction

Contact Information for Business Card

Open to ideas, we need 3 x different cards, one generic with no name and 2 x others each with 1 of our bosses name on each, I will put into upload files.

Colors
ec1f27
000000
606060
f5f5f5

Requirements
Must have
• Company Name and Logo
• Address
• Contact details, phone, website, email etc
• Small space to write notes when leaving card at residence
Nice to have
• Our motto "Servicing the Peninsula for over 35 years"

```html
<!DOCTYPE html>
<html lang="en">
<head>
<meta charset="utf-8">
<title>Brankel Rails – Business Cards</title>
<link href="https://fonts.googleapis.com/css2?family=Tinos:wght@400;700&display=swap" rel="stylesheet">
<style>
  :root {
    --red: #ec1f27;
    --black: #000000;
    --grey: #606060;
    --paper: #f5f5f5;
    --backdrop: #f2f2f2;
    --white: #ffffff;
    --fence-blue: #2f3f5c;
    --sky: #d9dfe6;
    --grass: #5a6240;
  }
  html, body {
    margin: 0; padding: 0;
    width: 1200px; height: 980px;
    overflow: hidden;
    background: var(--backdrop);
    font-family: "Tinos", "Times New Roman", serif;
  }
  .canvas { position: relative; width: 1200px; height: 980px; }
  .card {
    position: absolute; left: 355px;
    width: 515px; height: 305px;
    overflow: hidden;
  }
  .card--front { top: 170px; }
  .card--back { top: 540px; }
  .card__photo {
    position: absolute; inset: 0;
    background: linear-gradient(180deg, #3f5270 0%, #4a5f80 28%, var(--sky) 29%, #c9ced6 34%, var(--fence-blue) 38%, #34466a 84%, var(--grass) 92%, #6b7150 100%);
  }
  .brand-mark {
    position: absolute; display: flex; align-items: center; gap: 8px;
    font-weight: 700; letter-spacing: 1px; white-space: nowrap;
  }
  .brand-mark__dot { width: 14px; height: 14px; border-radius: 50%; background: var(--red); }
  .card--front .brand-mark {
    left: 50%; top: 72px; transform: translateX(-50%);
    color: var(--white); font-size: 26px;
  }
  .license__rule {
    position: absolute; left: 130px; top: 172px; width: 255px; height: 1px; background: var(--white);
  }
  .license {
    position: absolute; left: 0; right: 0; top: 173px; text-align: center;
    color: var(--white); font-size: 14px; letter-spacing: .3px;
  }
  .contact {
    position: absolute; top: 204px; color: var(--white);
    font-size: 10px; line-height: 12px; letter-spacing: 1px;
  }
  .contact--left { left: 23px; }
  .contact--right { left: 273px; }
  .contact__row { display: flex; white-space: nowrap; }
  .contact__label { width: 52px; }
  .motto-band {
    position: absolute; left: 0; right: 0; top: 260px; height: 30px;
    background: var(--black); color: var(--white);
    display: flex; align-items: center; justify-content: center;
    font-size: 11.5px; font-weight: 700; letter-spacing: 1px;
  }
  .card--back .card__photo { opacity: .75; }
  .notes-panel { position: absolute; inset: 0; }
  .card--back .brand-mark {
    left: 118px; top: 126px; color: var(--black); font-size: 26px;
  }
  .back-motto {
    position: absolute; left: 30px; top: 198px;
    font-size: 12.5px; font-weight: 700; letter-spacing: 1.2px; color: var(--black);
  }
</style>
</head>
<body>
<main class="canvas">

  <section class="card card--front">
    <div class="card__photo" role="img" aria-label="Photo of a dark blue steel fence with slat top in front of a house"></div>
    <div class="brand-mark"><span class="brand-mark__dot"></span>BRANKEL RAILS</div>
    <div class="license__rule"></div>
    <div class="license">GOLD LICENSE No. 52716k</div>
    <div class="contact contact--left">
      <div class="contact__row">Adress: 27 Harlow Ave Brankel</div>
      <div class="contact__row"><span class="contact__label">Ph:</span>43-508214</div>
      <div class="contact__row">PO Box 612 Marlow Bay NSW 2260</div>
    </div>
    <div class="contact contact--right">
      <div class="contact__row"><span class="contact__label">Office :</span>(02)43508214</div>
      <div class="contact__row"><span class="contact__label">Mobile:</span></div>
      <div class="contact__row"><span class="contact__label">E-mai:</span>office@brankelrails.com.au</div>
      <div class="contact__row"><span class="contact__label">Web:</span>www.brankelrails.com.au</div>
    </div>
    <div class="motto-band">"Servicing the Peninsula for over 35 years"</div>
  </section>

  <section class="card card--back">
    <div class="card__photo" role="img" aria-label="Faded photo of the blue steel fence and house"></div>
    <svg class="notes-panel" width="515" height="305" viewBox="0 0 515 305" aria-hidden="true">
      <rect x="19" y="16" width="477" height="274" fill="#ffffff" fill-opacity=".55"/>
      <polygon points="19,16 255,16 410,290 19,290" fill="#ffffff" fill-opacity=".55"/>
      <g stroke="#000000" stroke-width="1">
        <line x1="278" y1="43" x2="485" y2="43"/>
        <line x1="288" y1="64" x2="485" y2="64"/>
        <line x1="299" y1="86" x2="485" y2="86"/>
        <line x1="310" y1="107" x2="485" y2="107"/>
        <line x1="322" y1="128" x2="485" y2="128"/>
        <line x1="334" y1="150" x2="485" y2="150"/>
        <line x1="346" y1="171" x2="485" y2="171"/>
        <line x1="358" y1="193" x2="485" y2="193"/>
        <line x1="375" y1="214" x2="485" y2="214"/>
        <line x1="388" y1="236" x2="485" y2="236"/>
        <line x1="400" y1="257" x2="485" y2="257"/>
        <line x1="412" y1="279" x2="485" y2="279"/>
      </g>
    </svg>
    <div class="brand-mark"><span class="brand-mark__dot"></span>BRANKEL RAILS</div>
    <div class="back-motto">"Servicing the Peninsula for over 35 years"</div>
  </section>

</main>
</body>
</html>
```